Commercial photographer, UAV drone photography & 360 walk-through visuals

I need a business card design that is minimalist but yet pretentiously creative. My target market are architects, designers, advertising agents and marketing managers. It is important to stress that though I am asking for a minimalist design it needs to have creative impact.

Target Market(s)

Architects, interiors designers, web-designers, artists

Contact Information for Business Card

Include my name, mobile [cell] number, email, web page and the company logo. Do not to include a postal address.

Colors

Designer to choose colors to be used in the design.

Requirements
Must have
• The following information is to be included:
• Miles Perrow
• Photographer
• m: 07812 593174
• e: miles@mpframeworks.co.uk
• w: mpframeworks.co.uk

```html
<!DOCTYPE html>
<html lang="en">
<head>
<meta charset="utf-8">
<title>MP Frameworks – Business Card</title>
<link href="https://fonts.googleapis.com/css2?family=Open+Sans:wght@400;700&display=swap" rel="stylesheet">
<style>
  :root {
    --ink: #231f20;
    --paper: #ffffff;
    --swoosh: #8a8a8a;
    --backdrop: #e9e7e4;
    --text: #1f1b1c;
  }
  * { box-sizing: border-box; margin: 0; padding: 0; }
  html, body {
    width: 1200px; height: 900px; overflow: hidden;
    background: var(--backdrop);
    font-family: "Open Sans", Arial, sans-serif;
    color: var(--text);
  }
  .sheet {
    position: relative; width: 1200px; height: 900px;
    display: flex; flex-direction: column; align-items: center;
    justify-content: center; gap: 30px;
  }
  .card {
    position: relative; width: 700px; height: 400px; overflow: hidden;
    box-shadow: 0 6px 18px rgba(0,0,0,0.18);
  }
  .card--front { background: var(--ink); display: flex; align-items: center; justify-content: center; }
  .card--back { background: var(--paper); }

  .brand { display: flex; align-items: center; gap: 16px; }
  .brand__mark { width: 22px; height: 22px; border-radius: 50%; }
  .brand__name { font-weight: 400; letter-spacing: 5px; text-transform: uppercase; line-height: 1; white-space: nowrap; }
  .card--front .brand__mark { background: var(--paper); }
  .card--front .brand__name { color: var(--paper); font-size: 40px; }
  .card--back .brand { position: absolute; top: 78px; right: 48px; }
  .card--back .brand__mark { background: var(--ink); width: 18px; height: 18px; }
  .card--back .brand__name { color: var(--ink); font-size: 30px; }

  .wave { position: absolute; inset: 0; width: 100%; height: 100%; }

  .person { position: absolute; top: 88px; left: 50px; }
  .person__name { font-size: 21px; font-weight: 700; text-transform: uppercase; letter-spacing: -0.3px; line-height: 1.1; }
  .person__role { font-size: 16px; line-height: 1.2; }

  .contact { position: absolute; top: 182px; left: 86px; list-style: none; font-size: 17px; line-height: 24px; }
  .contact__item { display: flex; align-items: center; gap: 7px; white-space: nowrap; }
  .contact__icon { width: 14px; height: 14px; fill: var(--text); flex: none; }

  .website { position: absolute; right: 44px; top: 300px; color: var(--paper); font-size: 14px; white-space: nowrap; }
</style>
</head>
<body>
<main class="sheet">

  <section class="card card--front" aria-label="Card front">
    <div class="brand">
      <span class="brand__mark"></span>
      <span class="brand__name">MP Frameworks</span>
    </div>
  </section>

  <section class="card card--back" aria-label="Card back">
    <svg class="wave" viewBox="0 0 700 400" preserveAspectRatio="none" aria-hidden="true">
      <path fill="var(--swoosh)" d="M0,318 C190,344 310,318 410,262 C470,228 520,206 590,188 C520,214 470,246 400,290 C310,346 190,362 0,344 Z"/>
      <path fill="var(--ink)" d="M700,168 C570,184 480,230 410,284 C320,352 190,376 0,358 L0,400 L700,400 Z"/>
    </svg>

    <div class="person">
      <h1 class="person__name">Miles Perrow</h1>
      <p class="person__role">Photographer</p>
    </div>

    <div class="brand">
      <span class="brand__mark"></span>
      <span class="brand__name">MP Frameworks</span>
    </div>

    <ul class="contact">
      <li class="contact__item">
        <svg class="contact__icon" viewBox="0 0 16 16"><path d="M2 5c0-2 3-3 6-3s6 1 6 3v1h-3V5H5v1H2zM4 7h8l2 7H2z"/></svg>
        07812 593174
      </li>
      <li class="contact__item">
        <svg class="contact__icon" viewBox="0 0 16 16"><path d="M4 1h8v14H4zM5.5 3v9h5V3zM7 13h2v1H7z" fill-rule="evenodd"/></svg>
        07812 593175
      </li>
      <li class="contact__item">
        <svg class="contact__icon" viewBox="0 0 16 16"><path d="M1 3h14v10H1zM2 4l6 5 6-5z" fill-rule="evenodd"/></svg>
        miles@mpframeworks.co.uk
      </li>
    </ul>

    <p class="website">www.mpframeworks.co.uk</p>
  </section>

</main>
</body>
</html>
```